New modern business card design

To design a brand new business card that's clean & modern in terms of layout.
I have attached our company logo and also basic information regarding what is needed on the card that also needs to be editable.

Target Market(s)

motor trade

Contact Information for Business Card

logo, name, title, tel, mob, email, address, www, all information is in the word.doc file

Requirements
Must have
• white background
Nice to have
• Nice clean font

```html
<!DOCTYPE html>
<html lang="en">
<head>
<meta charset="utf-8">
<title>Torque Lift Ltd – Business Card</title>
<link href="https://fonts.googleapis.com/css2?family=Roboto:wght@300;400;500&display=swap" rel="stylesheet">
<style>
  :root{
    --page:#3a3a3c;
    --card-white:#ffffff;
    --ink:#2a2a2d;
    --blue:#1493dc;
    --grey-band:#a9a9ac;
    --rule:#9a9a9e;
    --white:#ffffff;
  }
  *{margin:0;padding:0;box-sizing:border-box}
  html,body{width:799px;height:1200px;overflow:hidden}
  body{background:var(--page);font-family:'Roboto',sans-serif;position:relative}
  .card{position:absolute;left:100px;width:600px;height:343px;border-radius:22px;overflow:hidden;background:var(--card-white)}
  .card--front{top:140px}
  .card--back{top:740px}

  /* front */
  .front-brand{position:absolute;top:118px;left:0;right:0;text-align:center}
  .brand-name{display:inline-flex;align-items:center;gap:12px;font-weight:500;font-size:34px;letter-spacing:3px;color:var(--ink);text-transform:uppercase}
  .brand-mark{width:16px;height:16px;background:var(--ink)}
  .brand-rule{width:360px;height:1px;background:var(--rule);margin:14px auto 0}
  .front-web{position:absolute;bottom:52px;left:0;right:0;display:flex;align-items:center;justify-content:center;gap:18px;font-size:16px;color:var(--ink)}
  .front-web .dash{width:60px;height:2px;background:var(--ink)}
  .front-web .accent{color:var(--blue)}

  /* back */
  .back-shape{position:absolute;inset:0}
  .back-brand{position:absolute;top:44px;left:150px}
  .back-brand .brand-name{color:var(--blue);font-size:28px;gap:10px}
  .back-brand .brand-mark{background:var(--blue);width:14px;height:14px}
  .back-brand .brand-rule{width:100%;background:var(--blue);margin:10px 0 0}
  .holder{position:absolute;left:28px;top:176px;color:var(--white)}
  .holder-name{font-size:25px;font-weight:500}
  .holder-title{font-size:11px;font-weight:300;margin-top:2px}
  .contacts{position:absolute;right:26px;top:216px;list-style:none;color:var(--white);font-size:12.5px;line-height:16px}
  .contacts li{display:flex;justify-content:flex-end;align-items:center;gap:8px}
  .contacts svg,.contacts .icon-gap{width:12px;height:12px;flex:none}
</style>
</head>
<body>

<section class="card card--front">
  <div class="front-brand">
    <div class="brand-name"><span class="brand-mark"></span>Torque Lift Ltd</div>
    <div class="brand-rule"></div>
  </div>
  <div class="front-web"><span class="dash"></span><span>www.<span class="accent">torque-lift</span>.co.uk</span><span class="dash"></span></div>
</section>

<section class="card card--back">
  <svg class="back-shape" viewBox="0 0 600 343" preserveAspectRatio="none">
    <path d="M0 138 C200 168 420 182 600 188 L600 202 C420 196 200 182 0 154 Z" fill="var(--grey-band)"/>
    <path d="M0 154 C200 182 420 196 600 202 L600 343 L0 343 Z" fill="var(--blue)"/>
  </svg>
  <div class="back-brand">
    <div class="brand-name"><span class="brand-mark"></span>Torque Lift Ltd</div>
    <div class="brand-rule"></div>
  </div>
  <div class="holder">
    <div class="holder-name">Daniel Morris</div>
    <div class="holder-title">General Manager</div>
  </div>
  <ul class="contacts">
    <li>0161 555 0142
      <svg viewBox="0 0 12 12"><path d="M2 1h3l1 3-2 1a7 7 0 0 0 3 3l1-2 3 1v3c-6 0-9-3-9-9z" fill="#fff"/></svg></li>
    <li>07700 900 318
      <svg viewBox="0 0 12 12"><rect x="3" y="0.5" width="6" height="11" rx="1" fill="#fff"/><rect x="4" y="2" width="4" height="7" fill="var(--blue)"/></svg></li>
    <li>dmorris@torque-lift.co.uk
      <svg viewBox="0 0 12 12"><rect x="0.5" y="2.5" width="11" height="7" fill="#fff"/><path d="M0.5 2.5 6 7l5.5-4.5" fill="none" stroke="var(--blue)"/></svg></li>
    <li>www.torque-lift.co.uk
      <svg viewBox="0 0 12 12"><circle cx="6" cy="6" r="5" fill="#fff"/><path d="M1 6h10M6 1c-3 3-3 7 0 10M6 1c3 3 3 7 0 10" fill="none" stroke="var(--blue)" stroke-width=".8"/></svg></li>
    <li>Kestrel Road Denton,<span class="icon-gap"></span></li>
    <li>Manchester M00 1AA
      <svg viewBox="0 0 12 12"><path d="M6 11C3 7 2 5.5 2 4.5a4 4 0 0 1 8 0C10 5.5 9 7 6 11z" fill="#fff"/><circle cx="6" cy="4.5" r="1.4" fill="var(--blue)"/></svg></li>
  </ul>
</section>

</body>
</html>
```